Recruiting agency looking for a newsletter design

We need to design a newsletter that will be sent by e-mail to our clients database. This communication announces a new milestone for our company.

We need it to convey high professionalism, elegance ad luxury. It needs to catch the reader’s attention.

The background needs to be light shiny silver, not flat gray, not dark silver. Some effects can give dimension to the content. We need a very impactful communication.

You will find attached:

- The content that needs to appear on the newsletter
- Pictures “moodboard” that you can take into consideration for the overall “atmosphere” and “emotion” that the design needs to convey. Please DO NOT include any of these images in the newsletter itself. They are just here to help you get the idea of the type of image we want to convey as a company with this communication.
- Company logo
- Please note that I will provide you later on with a URL link to include to the newsletter.

```html
<!DOCTYPE html>
<html lang="en">
<head>
<meta charset="utf-8">
<title>2021 New Era | New Fees</title>
<link rel="stylesheet" href="https://fonts.googleapis.com/css2?family=Orbitron:wght@800&family=Work+Sans:wght@400;700;800&family=Arimo:wght@400;700&display=swap">
<style>
  :root {
    --ink: #1b1b1b;
    --gold: #c79d32;
    --white: #ffffff;
    --muted: #555555;
    --rule: #a9a9a7;
    --line: #dddddd;
    --silver-hi: #f2f2f2;
    --silver-mid: #c9c9c9;
  }
  * { box-sizing: border-box; margin: 0; padding: 0; }
  html, body { width: 1200px; height: 1017px; overflow: hidden; background: var(--white); }
  body { position: relative; font-family: "Work Sans", sans-serif; color: var(--ink); }

  .preheader {
    position: absolute; top: 13px; left: 0; width: 1200px; text-align: center;
    font: 400 12px "Arimo", sans-serif; color: var(--muted);
  }
  .preheader a { color: var(--gold); text-decoration: none; }

  .hero { position: absolute; left: 350px; top: 42px; width: 500px; height: 675px; overflow: hidden; }
  .hero-rule { position: absolute; left: 0; width: 500px; height: 8px;
    background: linear-gradient(180deg, #c4c4c2, var(--rule) 60%, #8e8e8c); }
  .hero-rule.top { top: 0; }
  .hero-rule.bottom { bottom: 0; }
  .hero-photo { position: absolute; left: 0; top: 8px; width: 500px; height: 483px;
    background:
      radial-gradient(ellipse at 55% 30%, #ffffff 0%, #eeeeee 35%, transparent 70%),
      linear-gradient(180deg, #e8e8e8 0%, #dcdcdc 45%, #b8b8b8 75%, #8a8a8a 100%); }
  .hero-silver { position: absolute; left: 0; top: 491px; width: 500px; height: 176px;
    background:
      linear-gradient(115deg, transparent 30%, rgba(255,255,255,.7) 45%, transparent 60%),
      linear-gradient(180deg, var(--silver-mid), var(--silver-hi) 55%, var(--silver-mid) 100%);
    border-top: 6px solid #a6a6a4; }

  .year { position: absolute; top: 40px; width: 500px; text-align: center;
    font: 800 60px/1 "Orbitron", sans-serif; letter-spacing: 2px; color: var(--ink); }
  .headline { position: absolute; top: 113px; width: 500px; text-align: center;
    font: 800 41px/1 "Work Sans", sans-serif; color: var(--ink); white-space: nowrap; }
  .headline .divider { display: inline-block; width: 8px; height: 42px; background: var(--ink);
    border-radius: 3px; vertical-align: -6px; margin: 0 10px; }

  .fee-card { position: absolute; top: 320px; width: 213px; height: 213px; background: var(--white); padding: 8px; }
  .fee-card.managers { left: 25px; }
  .fee-card.others { left: 262px; }
  .fee-photo { position: relative; width: 100%; height: 100%; overflow: hidden; }
  .managers .fee-photo { background: linear-gradient(160deg, #5b5570 0%, #8a6e58 35%, #3a3630 70%, #1e1e1e 100%); }
  .others .fee-photo { background: radial-gradient(circle at 70% 40%, #4a4a4a 0%, #242424 50%, #141414 100%); }
  .fee-rate { position: absolute; left: 7px; top: 98px; font: 800 36px/1 "Work Sans", sans-serif; color: var(--white); letter-spacing: 1px; }
  .fee-label { position: absolute; left: 8px; padding: 0 8px; height: 24px;
    font: 800 18.5px/24px "Work Sans", sans-serif; letter-spacing: .5px; white-space: nowrap; }
  .fee-label.dark { top: 139px; background: var(--ink); color: var(--white); }
  .fee-label.light { top: 163px; background: var(--white); color: var(--ink); }

  .join-btn { position: absolute; left: 187px; top: 565px; width: 125px; height: 42px;
    background: var(--gold); color: var(--white); text-align: center;
    font: 800 19px/42px "Work Sans", sans-serif; text-decoration: none; }
  .tagline { position: absolute; top: 620px; width: 500px; text-align: center;
    font: 700 19px/1 "Work Sans", sans-serif; color: var(--ink); }

  .info { position: absolute; left: 350px; top: 717px; width: 500px; height: 145px;
    border: 1px solid var(--line); border-top: none; background: var(--white); }
  .info-title { position: absolute; left: 23px; top: 30px; font: 400 20px/1 "Work Sans", sans-serif; letter-spacing: .5px; }
  .info-btn { position: absolute; left: 25px; top: 65px; width: 158px; height: 42px;
    background: var(--gold); color: var(--white); text-align: center;
    font: 800 19px/42px "Arimo", sans-serif; text-decoration: none; }
  .brand { position: absolute; right: 25px; top: 86px; display: flex; align-items: center; gap: 8px;
    font: 700 14px/1 "Work Sans", sans-serif; letter-spacing: 2px; color: var(--ink); }
  .brand-dot { width: 12px; height: 12px; border-radius: 50%; background: var(--ink); }

  .shadow { position: absolute; left: 360px; top: 862px; width: 480px; height: 22px;
    background: radial-gradient(ellipse at 50% 0%, rgba(0,0,0,.35) 0%, rgba(0,0,0,0) 70%); }

  .footer { position: absolute; top: 893px; left: 0; width: 1200px; text-align: center;
    font: 400 10.5px/20px "Arimo", sans-serif; color: var(--muted); }
  .footer b { font-weight: 700; }
  .unsubscribe { position: absolute; top: 972px; left: 0; width: 1200px; text-align: center;
    font: 700 10.5px/1 "Arimo", sans-serif; }
  .unsubscribe a { color: var(--gold); text-decoration: none; }
</style>
</head>
<body>
  <p class="preheader">If you are unable to view this message correctly, <a href="#">click here</a></p>

  <section class="hero">
    <div class="hero-photo" role="img" aria-label="Bright modern open-plan office with white desks, monitors and a potted plant"></div>
    <div class="hero-silver"></div>
    <div class="hero-rule top"></div>
    <div class="hero-rule bottom"></div>

    <h1 class="year">2021</h1>
    <h2 class="headline">NEW ERA<span class="divider"></span>NEW FEES</h2>

    <div class="fee-card managers">
      <div class="fee-photo" role="img" aria-label="Luxury car side view at sunset">
        <span class="fee-rate">25%</span>
        <span class="fee-label dark">TOP MANGERS</span>
        <span class="fee-label light">EXECUTIVES</span>
      </div>
    </div>
    <div class="fee-card others">
      <div class="fee-photo" role="img" aria-label="Close-up of a steel chronograph wristwatch">
        <span class="fee-rate">21%</span>
        <span class="fee-label dark">ALL OTHER</span>
        <span class="fee-label light">APPOINTMENTS</span>
      </div>
    </div>

    <a class="join-btn" href="#">JOIN US</a>
    <p class="tagline">In shaping the future of recruitment</p>
  </section>

  <section class="info">
    <p class="info-title">For More information</p>
    <a class="info-btn" href="#">CLICK HERE</a>
    <div class="brand"><span class="brand-dot"></span>CORVANE &amp; PARTNERS</div>
  </section>
  <div class="shadow"></div>

  <footer class="footer">
    <p>Copyright © 2020 <b>Corvane &amp; Partners.</b> All Rights Reserved.</p>
    <p><b>USA Headquarters:</b> 18 Harbor Row, Boston, MA 02110 | <b>Phone:</b> +1 (617) 555-0142</p>
    <p><b>European Headquarters:</b> 14 Rue des Lilas, Paris, France, 75011 | <b>Phone:</b> +33 1 55 50 12 40</p>
  </footer>
  <p class="unsubscribe"><a href="#">Unsubscribe</a></p>
</body>
</html>
```